Larkspur Realty

Business cards for 4 people

They need to say for all
57 Danner Quay, Boston MA 02117

Each person will have their own personal information
We would like gold embossing for the name of the company
Mabel is the blonde sitting in the chair smiling her information should be on the back of the card with her name and information
Should say for slogan Timeless Homes, Refined Service
mabel@larkspurhomesnet.com
(413) 555-0182

Odessa is the brunette with wavy hair in the tan suit odessa@larkspurhomesnet.com
(617) 555-0147

june@larkspurhomesnet.com
(413) 555-0169
standing next to the chair

ruth@larkspurhomesnet.com
(413) 555-0193
close up headshot

```html
<!DOCTYPE html>
<html lang="en">
<head>
<meta charset="utf-8">
<title>Larkspur Realty — Business Cards</title>
<link rel="stylesheet" href="https://fonts.googleapis.com/css2?family=Cinzel:wght@600;700&family=Montserrat:wght@400;500&display=swap">
<style>
  :root {
    --navy: #1e2d4d;
    --navy-deep: #18253f;
    --gold: #c9a052;
    --gold-light: #f0d38c;
    --gold-dark: #9c7430;
    --white: #f4f4f6;
    --backdrop: #e9e6e1;
    --photo-light: #d9d9db;
    --photo-dark: #3a2c26;
  }
  * { box-sizing: border-box; margin: 0; padding: 0; }
  html, body { width: 1200px; height: 900px; overflow: hidden; }
  body {
    background: var(--backdrop);
    display: flex;
    flex-direction: column;
    align-items: center;
    justify-content: center;
    gap: 40px;
  }
  .card {
    position: relative;
    width: 700px;
    height: 400px;
    background: var(--navy);
    overflow: hidden;
    box-shadow: 0 8px 22px rgba(0,0,0,.25);
  }
  .gold-band {
    position: absolute;
    left: 0; right: 0;
    background: linear-gradient(180deg, var(--gold-dark) 0%, var(--gold-light) 45%, var(--gold) 70%, var(--gold-dark) 100%);
    display: flex;
    align-items: center;
    justify-content: center;
  }

  /* Front */
  .card-front { display: flex; }
  .agent-photo {
    width: 262px;
    height: 100%;
    background: linear-gradient(160deg, var(--photo-light) 0%, #b9b3b0 35%, #6b5247 60%, var(--photo-dark) 100%);
  }
  .front-info {
    position: relative;
    flex: 1;
    text-align: center;
  }
  .brand {
    display: flex;
    flex-direction: column;
    align-items: center;
    gap: 10px;
  }
  .brand-circle {
    border: 2px solid var(--gold);
    border-radius: 50%;
  }
  .brand-name {
    font-family: "Cinzel", serif;
    font-weight: 700;
    color: var(--gold);
    letter-spacing: 1px;
    white-space: nowrap;
  }
  .front-info .brand { margin-top: 30px; }
  .front-info .brand-circle { width: 56px; height: 56px; }
  .front-info .brand-name { font-size: 24px; }
  .agent-name {
    margin-top: 20px;
    font-family: "Cinzel", serif;
    font-weight: 700;
    font-size: 18px;
    color: var(--gold);
    letter-spacing: 1px;
  }
  .contact-list {
    list-style: none;
    margin-top: 16px;
    display: flex;
    flex-direction: column;
    align-items: center;
    gap: 7px;
    font-family: "Montserrat", sans-serif;
    font-size: 13px;
    color: var(--white);
  }
  .contact-list li { display: flex; align-items: center; gap: 7px; }
  .contact-list svg { width: 13px; height: 13px; fill: var(--gold); flex: none; }
  .card-front .gold-band { top: 302px; height: 34px; }
  .slogan {
    font-family: "Cinzel", serif;
    font-weight: 700;
    font-size: 12px;
    letter-spacing: 1px;
    color: var(--navy-deep);
  }

  /* Back */
  .card-back .brand {
    position: absolute;
    top: 60px; left: 0; right: 0;
    gap: 16px;
  }
  .card-back .brand-circle { width: 100px; height: 100px; border-width: 3px; }
  .card-back .brand-name { font-size: 40px; letter-spacing: 2px; }
  .card-back .gold-band { top: 292px; height: 40px; }
  .website {
    font-family: "Montserrat", sans-serif;
    font-weight: 500;
    font-size: 14px;
    color: var(--navy-deep);
  }
</style>
</head>
<body>

  <section class="card card-front">
    <div class="agent-photo" role="img" aria-label="Portrait photo of agent Ruth, close-up headshot against a light grey wall"></div>
    <div class="front-info">
      <div class="brand">
        <span class="brand-circle"></span>
        <span class="brand-name">LARKSPUR REALTY</span>
      </div>
      <h1 class="agent-name">RUTH</h1>
      <ul class="contact-list">
        <li>
          <svg viewBox="0 0 16 16" aria-hidden="true"><path d="M4 0h8a1.5 1.5 0 0 1 1.5 1.5v13A1.5 1.5 0 0 1 12 16H4a1.5 1.5 0 0 1-1.5-1.5v-13A1.5 1.5 0 0 1 4 0zm.5 2v11h7V2zm3.5 11.6a.9.9 0 1 0 0 1.8.9.9 0 0 0 0-1.8z"/></svg>
          (413) 555-0193
        </li>
        <li>
          <svg viewBox="0 0 16 16" aria-hidden="true"><path d="M0 3h16v10H0zm1.5 1.2v.3L8 9l6.5-4.5v-.3zm0 2.1v5.2h13V6.3L8 10.8z"/></svg>
          ruth@larkspurhomesnet.com
        </li>
        <li>
          <svg viewBox="0 0 16 16" aria-hidden="true"><path d="M8 0a5.5 5.5 0 0 1 5.5 5.5C13.5 10 8 16 8 16S2.5 10 2.5 5.5A5.5 5.5 0 0 1 8 0zm0 3a2.5 2.5 0 1 0 0 5 2.5 2.5 0 0 0 0-5z"/></svg>
          57 Danner Quay, Boston MA 02117
        </li>
      </ul>
      <div class="gold-band">
        <span class="slogan">TIMELESS HOMES, REFINED SERVICE</span>
      </div>
    </div>
  </section>

  <section class="card card-back">
    <div class="brand">
      <span class="brand-circle"></span>
      <span class="brand-name">LARKSPUR REALTY</span>
    </div>
    <div class="gold-band">
      <span class="website">www.larkspurhomesnet.com</span>
    </div>
  </section>

</body>
</html>
```